Stationery Design for Tierhaven

We already have a logo a Logo for our outstanding veterinary hospital. Now we are looking for our future letterhead, business cards and envelopes. We would like to see a design using the color from our logo. Additional color should be limited to grey or a rusty brown. The font should be easy and clearly readable and must be easily available on all computers (to install it in our Management software). The finial design should communicate competence in veterinary medicine, and empathy.

To meet the European regulation (DIN5008) there are a couple mandatory legal informations one the letterhead. We also enclosed a template of exact measurement, which need to be respected according to DIN5008.

Mandatory legal information are (best placed in the footer):
"Tierhaven GmbH & Co KG, Ostrowgasse 417C, 1230 Wien,
Handelsgericht Wien, FN 924615k, GF: Dr. Lukas Brandl
ATU 3148926"
Additional informations needed:
"Tel: +43 1 5849163, Fax: +43 1 5849164, info@tierhaven-example.at, www. tierhaven-example.at"
bank account informations should be included as well. These are:
"Sparkasse Obergruntal, IBAN: AT 58 1111 2222 3333 4444, BIC: SPKTAT4K817"

The Logo should be in the upper right corner. Below that we need a space for informations regarding the responsible veterinarians. There will be 3-5 Names, each of it consisting of 2 lines (see example below). The Names should be highlighted (larger font) compared to the qualifications in the second line.
Tierärztliche Leitung:
Dr. Lukas Brandl
Diplomate ECVS

The contest was startet on the 2nd of may and the deadline was a day later? Why was that so fast? Did I do something wrong? BR

Target Market(s)

dog and cat owner in Austria as welle as referring veterinarians in Austria

Industry/Entity Type

Veterinary

Contact Information for Business Card

One side: Logo
other side:
Dr. Lukas Brandl
Diplomate ECVS
EBVS Specialist of Small Animal Surgery

Tierhaven GmbH&Co KG
Ostrowgasse 417C
1230 Wien

Tel: +43 1 6210000 DW 102
Fax: +43 1 6210000 DW 999
email: lukas.brandl@tierhaven-example.at

Font styles to use
Serif
Sans Serif

Requirements
Must have
• The logo should be given in the upper right. Most of the legal informations should be given in the footer. The upper left Area should be clear, since the recipient address will be placed there.
Colors should be limited to golden, blue and greyscale (two different gereysacales at most).

```html
<!DOCTYPE html>
<html lang="de">
<head>
<meta charset="utf-8">
<title>Tierhaven – Visitenkarte</title>
<link href="https://fonts.googleapis.com/css2?family=Red+Hat+Display:wght@400;500;700;800&display=swap" rel="stylesheet">
<style>
  :root {
    --navy: #121d4a;
    --gold: #c9980f;
    --paper: #f2f2f2;
    --ink: #2f2f33;
    --backdrop: #cfcfcf;
  }
  * { margin: 0; padding: 0; box-sizing: border-box; }
  html, body { width: 1200px; height: 800px; overflow: hidden; }
  body {
    background: var(--backdrop);
    font-family: "Red Hat Display", Arial, sans-serif;
    position: relative;
  }
  .card {
    position: absolute;
    top: 233px;
    width: 520px;
    height: 334px;
    overflow: hidden;
  }
  .card--contact { left: 50px; background: var(--paper); }
  .card--brand { left: 630px; background: var(--navy); }

  /* contact side */
  .name-band {
    position: absolute;
    left: 0; top: 49px;
    width: 400px; height: 80px;
    background: var(--navy);
    padding: 9px 0 0 45px;
  }
  .person-name {
    color: var(--gold);
    font-weight: 800;
    font-size: 22px;
    letter-spacing: 0.3px;
    line-height: 1.2;
  }
  .qualification {
    color: var(--gold);
    font-size: 14.5px;
    line-height: 1.3;
    letter-spacing: 0.2px;
  }
  .badge {
    position: absolute;
    left: 374px; top: 30px;
    width: 118px; height: 118px;
    border-radius: 50%;
    background: var(--paper);
    display: flex; align-items: center; justify-content: center;
  }
  .badge-circle {
    width: 104px; height: 104px;
    border-radius: 50%;
    background: var(--navy);
    border: 3px solid var(--gold);
    display: flex; align-items: center; justify-content: center;
  }
  .badge-name {
    color: #fff;
    font-weight: 700;
    font-size: 15px;
  }
  .contact {
    position: absolute;
    left: 45px; top: 150px;
    color: var(--ink);
    font-size: 15.5px;
    line-height: 1.25;
    letter-spacing: 0.2px;
  }
  .contact p + p { margin-top: 11px; }
  .label { font-weight: 800; font-size: 11.5px; letter-spacing: 0.5px; }
  .web { font-weight: 800; color: var(--navy); }

  /* brand side */
  .brand {
    position: absolute;
    inset: 0;
    display: flex; align-items: center; justify-content: center;
    gap: 26px;
  }
  .brand-circle {
    width: 130px; height: 130px;
    border-radius: 50%;
    background: #f3f3f3;
    border: 3px solid var(--gold);
    box-shadow: 0 0 0 6px var(--navy), 0 0 0 9px var(--gold);
    border-color: var(--navy);
  }
  .brand-name {
    color: #fff;
    font-weight: 800;
    font-size: 50px;
    line-height: 1;
    letter-spacing: -0.5px;
  }
  .brand-tagline {
    color: var(--gold);
    font-weight: 500;
    font-size: 20px;
    margin-top: 8px;
    letter-spacing: 0.3px;
  }
</style>
</head>
<body>
  <section class="card card--contact">
    <div class="name-band">
      <h1 class="person-name">DR. LUKAS BRANDL</h1>
      <p class="qualification">Diplomate ECVS</p>
      <p class="qualification">EBVS Specialist of Small Animal Surgery</p>
    </div>
    <div class="badge">
      <div class="badge-circle"><span class="badge-name">Tierhaven</span></div>
    </div>
    <div class="contact">
      <p>+43 1 5849163 <span class="label">TEL</span><br>
         +43 1 5849164 <span class="label">FAX</span><br>
         lukas.brandl@tierhaven-example.at</p>
      <p>Tierhaven GmbH&amp;Co KG<br>
         Ostrowgasse 417C<br>
         1230 Wien</p>
      <p class="web">www.tierhaven-example.at</p>
    </div>
  </section>

  <section class="card card--brand">
    <div class="brand">
      <div class="brand-circle"></div>
      <div>
        <p class="brand-name">Tierhaven</p>
        <p class="brand-tagline">Fachklinik für Kleintiere</p>
      </div>
    </div>
  </section>
</body>
</html>
```